ORV Holding

ORV holding is located in the UAE. In the company, there are several departments covering Hospitality management, Facility Management, interior design and Construction.

The logo should not include the name holding, Just ORV.

Needed Items:

(1) Logo.
(2) Business Card.
(3) Letterhead
(4) Envelope
(5) cd cover
(6) email signature
Updates

The previous brief was misplaced with another competition. Current update is the final.

Target Market(s)

Collaboration with international high end firms.

Industry/Entity Type

Business

Requirements
Must have
• COLOR PREFERENCE Maximum 2 colors, preferably mono-color with different shades.
Nice to have
• Elegant, luxurious, and minimalistic.

```html
<!DOCTYPE html>
<html lang="en">
<head>
<meta charset="utf-8">
<title>ORV Stationery Set</title>
<link rel="stylesheet" href="https://fonts.googleapis.com/css2?family=Open+Sans:wght@400;600&display=swap">
<style>
:root{
  --bg:#e6e7e9;
  --dark:#353334;
  --white:#ffffff;
  --blue:#2788b5;
  --cyan:#00adef;
  --silver:#c4c5c7;
  --ink:#353334;
}
*{margin:0;padding:0;box-sizing:border-box}
html,body{width:1200px;height:810px;overflow:hidden;background:var(--bg);font-family:"Open Sans",sans-serif;color:var(--ink)}
.sheet{position:absolute;overflow:hidden;background:var(--dark)}
.sheet svg.shape{position:absolute;inset:0;width:100%;height:100%}
.abs{position:absolute}
.wordmark{position:absolute;font-weight:600;letter-spacing:-1px;line-height:1}
.contact{position:absolute;font-size:7.5px;line-height:12.6px;white-space:nowrap}
.contact .row::after{content:"";display:inline-block;width:1.3px;height:6px;background:var(--cyan);margin-left:2px;vertical-align:-0.5px}
.name{font-weight:600;font-size:11px;line-height:11px}
.title{font-size:8px;line-height:10px}

.card-front{left:28px;top:43px;width:270px;height:158px}
.card-back{left:34px;top:231px;width:270px;height:158px}
.cd-cover{left:364px;top:35px;width:379px;height:350px}
.letterhead{left:782px;top:39px;width:390px;height:554px;background:var(--white)}
.envelope{left:26px;top:430px;width:745px;height:335px}

.cd-cover .wordmark{left:-18px;top:150px;font-size:262px;color:var(--blue);letter-spacing:-8px;line-height:.78}

.letterhead .band{position:absolute;inset:0;width:100%;height:130px}
.letterhead .logo-tile{position:absolute;left:24px;top:0;width:72px;height:62px;background:var(--white)}
.letterhead .contact{color:var(--white);text-align:right;right:13px;top:36px;font-size:8.5px;line-height:14px}
.letterhead .contact .row::after{background:var(--white)}

.envelope .contact{font-size:14px;line-height:22px;left:219px;top:250px}
.envelope .contact .row::after{display:none}
.envelope .contact .bar{display:inline-block;width:2px;height:10px;background:var(--cyan);margin:0 5px 0 0;vertical-align:-0.5px}
</style>
</head>
<body>

<section class="sheet card-front">
  <svg class="shape" viewBox="0 0 270 158" preserveAspectRatio="none" aria-hidden="true">
    <defs><linearGradient id="edge1" x1="0" y1="0" x2="0" y2="1"><stop offset="0" stop-color="#dcdddf"/><stop offset=".6" stop-color="#a7a9ac"/><stop offset="1" stop-color="#e4e5e6"/></linearGradient></defs>
    <path d="M172,0 C120,28 85,68 85,105 C85,132 112,150 140,158 L270,158 L270,0 Z" fill="var(--white)" stroke="url(#edge1)" stroke-width="3"/>
  </svg>
  <div class="wordmark" style="left:10px;top:90px;font-size:36px;color:var(--white)">ORV</div>
  <div class="abs" style="right:52px;top:12px;text-align:right">
    <div class="name">abc</div><div class="title">designation</div>
  </div>
  <div class="contact" style="right:50px;top:98px;text-align:right">
    <div class="row">address</div><div class="row">000 000 0000</div><div class="row">info@orvmail.com</div><div class="row">www.orv.com</div>
  </div>
</section>

<section class="sheet card-back">
  <svg class="shape" viewBox="0 0 270 158" preserveAspectRatio="none" aria-hidden="true">
    <defs><linearGradient id="edge2" x1="0" y1="0" x2="0" y2="1"><stop offset="0" stop-color="#dcdddf"/><stop offset=".6" stop-color="#a7a9ac"/><stop offset="1" stop-color="#e4e5e6"/></linearGradient></defs>
    <path d="M188,0 C135,30 94,72 94,104 C94,132 128,150 160,158 L270,158 L270,0 Z" fill="var(--white)" stroke="url(#edge2)" stroke-width="3"/>
  </svg>
  <div class="wordmark" style="left:14px;top:69px;font-size:34px;color:var(--white)">ORV</div>
  <div class="abs" style="left:125px;top:62px">
    <div class="name">abc</div><div class="title">designation</div>
  </div>
  <div class="contact" style="right:11px;top:98px;text-align:right">
    <div class="row">address</div><div class="row">000 000 0000</div><div class="row">info@orvmail.com</div><div class="row">www.orv.com</div>
  </div>
</section>

<section class="sheet cd-cover">
  <div class="wordmark">ORV</div>
</section>

<section class="sheet letterhead">
  <svg class="band" viewBox="0 0 390 130" preserveAspectRatio="none" aria-hidden="true">
    <defs><linearGradient id="edge3" x1="0" y1="0" x2="1" y2="0"><stop offset="0" stop-color="#b0b2b4"/><stop offset=".5" stop-color="#e6e7e8"/><stop offset="1" stop-color="#a7a9ac"/></linearGradient></defs>
    <path d="M0,0 L390,0 L390,120 C300,80 200,44 96,46 C60,48 20,62 0,75 Z" fill="var(--dark)"/>
    <path d="M0,75 C20,62 60,48 96,46 C200,44 300,80 390,120" fill="none" stroke="url(#edge3)" stroke-width="4"/>
  </svg>
  <div class="logo-tile"></div>
  <div class="wordmark" style="left:24px;top:72px;font-size:38px;color:var(--blue)">ORV</div>
  <div class="contact">
    <div class="row">address</div>
    <div><span class="row">000 000 0000</span> <span class="row">info@orvmail.com</span></div>
    <div class="row">www.orv.com</div>
  </div>
</section>

<section class="sheet envelope">
  <svg class="shape" viewBox="0 0 745 335" preserveAspectRatio="none" aria-hidden="true">
    <defs><linearGradient id="edge4" x1="0" y1="0" x2="0" y2="1"><stop offset="0" stop-color="#dcdddf"/><stop offset=".65" stop-color="#a7a9ac"/><stop offset="1" stop-color="#e4e5e6"/></linearGradient></defs>
    <path d="M289,0 C170,88 90,168 90,226 C90,280 150,318 209,335 L745,335 L745,0 Z" fill="var(--white)" stroke="url(#edge4)" stroke-width="5"/>
  </svg>
  <div class="wordmark" style="left:23px;top:98px;font-size:48px;color:var(--blue)">ORV</div>
  <div class="contact">
    <div><span class="bar"></span>address</div>
    <div><span class="bar"></span>000 000 0000 <span class="bar"></span>info@orvmail.com</div>
    <div><span class="bar"></span>www.orv.com</div>
  </div>
</section>

</body>
</html>
```